Business cards and logo for kitchen and bath remodeling company

We want an elegant card but that calls attention something unique and when people see it they remember us. A log that we can use for our own. We are a kitchen and bathroom remodeling company. We are 3 partners staring the company we are located in seattle washington usa. We try to give the best experience and luxury look in our projects and we are looking to show that in our cards. I added a sample of a card I really like. I like the black and gold look but gray blue or green in a metallic look would look nice. I'm open to any color.

Target Market(s)

Home owners.

Industry/Entity Type

Construction

Contact Information for Business Card

Copperfern builders

Colors

Designer to choose colors to be used in the design.

Requirements
Must have
• Make a Logo
• Logo to be unique
• Name of company copperfern builders
Nice to have
• Have a good color scheme
• Front design to connect with back of card

```html
<!DOCTYPE html>
<html lang="en">
<head>
<meta charset="utf-8">
<title>Copperfern Builders – Business Card</title>
<link rel="stylesheet" href="https://fonts.googleapis.com/css2?family=Montserrat:wght@500;600&family=Arimo:wght@400&display=swap">
<style>
  :root {
    --backdrop: #b9b9b9;
    --card: #151515;
    --card-back: #0f0f0f;
    --gold: #c9ad8a;
    --gold-light: #e8d8c2;
    --gold-dark: #8a6f52;
    --text: #ffffff;
  }
  * { margin: 0; padding: 0; box-sizing: border-box; }
  html, body { width: 1200px; height: 802px; overflow: hidden; }
  body {
    background: var(--backdrop);
    position: relative;
    font-family: "Arimo", Arial, sans-serif;
  }
  .card {
    position: absolute;
    top: 274px;
    width: 443px;
    height: 263px;
    background: var(--card);
    box-shadow: 0 3px 8px rgba(0,0,0,0.35);
    overflow: hidden;
  }
  .card--front { left: 136px; }
  .card--back { left: 624px; background: var(--card-back); }
  .card__band {
    position: absolute;
    left: 0; right: 0; bottom: 0;
    height: 6px;
    background: linear-gradient(90deg, var(--gold-dark), var(--gold-light) 45%, var(--gold) 70%, var(--gold-dark));
  }
  .brand {
    position: absolute;
    text-align: center;
    font-family: "Montserrat", sans-serif;
    font-weight: 600;
    color: var(--gold);
  }
  .brand--front { left: 216px; width: 208px; top: 96px; }
  .brand__mark {
    display: inline-flex;
    align-items: center;
    gap: 7px;
    font-size: 27px;
    letter-spacing: 1px;
    white-space: nowrap;
  }
  .brand--front .brand__mark { font-size: 20px; letter-spacing: 0.5px; gap: 6px; }
  .brand__square {
    width: 14px; height: 14px;
    background: var(--gold);
  }
  .brand--front .brand__square { width: 11px; height: 11px; }
  .brand__rule {
    display: flex;
    align-items: center;
    gap: 8px;
    margin-top: 4px;
    font-size: 10.5px;
    letter-spacing: 2.5px;
  }
  .brand__rule::before, .brand__rule::after {
    content: "";
    flex: 1;
    height: 1px;
    background: var(--gold);
  }
  .brand--back { left: 0; right: 0; top: 112px; }
  .brand--back .brand__mark { font-size: 30px; }
  .person {
    position: absolute;
    left: 27px;
    top: 148px;
  }
  .person__name {
    font-family: "Montserrat", sans-serif;
    font-weight: 600;
    font-size: 15px;
    color: var(--gold);
    letter-spacing: 0.3px;
  }
  .person__title { font-size: 12.5px; color: var(--text); margin-top: 1px; }
  .contacts {
    position: absolute;
    left: 27px;
    top: 192px;
    list-style: none;
    font-size: 12.5px;
    color: var(--text);
    line-height: 16.5px;
  }
  .contacts li { display: flex; align-items: center; gap: 4px; }
  .contacts svg { width: 11px; height: 11px; fill: var(--gold); }
  .address {
    position: absolute;
    right: 21px;
    top: 208px;
    text-align: right;
    font-style: normal;
    font-size: 12.5px;
    line-height: 16px;
    color: var(--text);
  }
</style>
</head>
<body>
  <section class="card card--front">
    <div class="brand brand--front">
      <div class="brand__mark"><span class="brand__square"></span>COPPERFERN</div>
      <div class="brand__rule">BUILDERS</div>
    </div>
    <div class="person">
      <p class="person__name">MARCUS HALE</p>
      <p class="person__title">Managing Director</p>
    </div>
    <ul class="contacts">
      <li><svg viewBox="0 0 24 24"><path d="M6.6 10.8a15 15 0 0 0 6.6 6.6l2.2-2.2a1 1 0 0 1 1-.25 11.4 11.4 0 0 0 3.6.57 1 1 0 0 1 1 1V20a1 1 0 0 1-1 1A17 17 0 0 1 3 4a1 1 0 0 1 1-1h3.5a1 1 0 0 1 1 1c0 1.25.2 2.45.57 3.57a1 1 0 0 1-.25 1z"/></svg>044-987 654 321</li>
      <li><svg viewBox="0 0 24 24"><path d="M2 5h20v14H2z M2 5l10 8 10-8" /></svg>hello@copperfern.com</li>
      <li><svg viewBox="0 0 24 24"><path d="M12 2a10 10 0 1 0 0 20 10 10 0 0 0 0-20zm0 2c1.3 1.5 2.2 3.6 2.4 7H9.6c.2-3.4 1.1-5.5 2.4-7zM4.1 13h3.5c.1 2.4.6 4.4 1.4 6A8 8 0 0 1 4.1 13zm0-2A8 8 0 0 1 9 5c-.8 1.6-1.3 3.6-1.4 6zm5.5 2h4.8c-.2 3.4-1.1 5.5-2.4 7-1.3-1.5-2.2-3.6-2.4-7zm6.8 0h3.5a8 8 0 0 1-4.9 6c.8-1.6 1.3-3.6 1.4-6zm0-2c-.1-2.4-.6-4.4-1.4-6a8 8 0 0 1 4.9 6z"/></svg>www.copperfernbuilders.com</li>
    </ul>
    <address class="address">87, Harbor Lane West<br>Seattle WA, 98101</address>
    <div class="card__band"></div>
  </section>

  <section class="card card--back">
    <div class="brand brand--back">
      <div class="brand__mark"><span class="brand__square"></span>COPPERFERN</div>
    </div>
    <div class="card__band"></div>
  </section>
</body>
</html>
```